Business Card Design Project

*****This is part of another project please look at that as well when considering the business cards I have copy and pasted that project below and will provide specif business card info in the other fields******
Pine Ledger LLC is a licensed general contractor and roofing company. We would like a logo/ door hanger designed for the expressed purpose of canvasing (door knocking). A professional and sleek appearance is going to be required. We would like the flyer to be predominately focused on roofs. We only canvass areas that have a specific types of damage; wind and hail damage. You can read more about wind and hail damage here : https://galeroofguide.example/spot-weather-harm.php
If you need more of an idea of what kind of customers we are targeting or we are trying to acquire as customers.

A little about our company. We are dedicated to our customer and making sure that they get the best roof or general contracting experience possible. We believe in doing things the right way we are not about taking short cuts. In roofing this is absolutely necessary because most people know next to nothing about a roof. On wind and hail insurance claims give all of customer a 2 free upgrades we only use architectural shingles and a synthetic underlamenate. We use only Varnholt Ridgeline shingles

For the logo I have an idea of a house with a stethoscope maybe in cartoon form but it has to be professional. I'm flexible on this idea as you guys are the design pros.

Please keep in mind on the door hangers that there will be a cut out where it attaches to the door so that should be worked into the design. They will be printed on 4.25" x 11" which is a standard size. We plan on getting them printed at https://www.knobcardprints.example/category which you can go to if you need the template.
Updates

License number qbx5074316 and qbz6081453 must be included along with licensed and insured

Target Market(s)

primarily roof customers as well as residential remodel customers

Industry/Entity Type

Contractor

Font styles to use
Other font styles liked:
• I don't know not fancy or cursive, but not to common either I want it to stand out

Requirements
Must have
• Neat, clean, sleek ----a logo line which i don't have fore you. I really want people to know that if they are experiancing any roof issues or roof damage we are the poeple to talk to. Would like a cool font but not to cool.
Nice to have
• house with a stethiscope something drawn not a photo.
Should not have
• just keep it professional.

```html
<!DOCTYPE html>
<html lang="en">
<head>
<meta charset="utf-8">
<title>Pine Ledger LLC – Door Hanger</title>
<link rel="stylesheet" href="https://fonts.googleapis.com/css2?family=Open+Sans:wght@400;600;700&display=swap">
<style>
  :root {
    --stage: #c4c4c4;
    --sky: #29a8e0;
    --cloud-white: #ffffff;
    --grass: #8cc63f;
    --brand-red: #e1262b;
    --ink: #1e1e1e;
    --rule-gray: #a7a9ac;
  }
  * { box-sizing: border-box; margin: 0; padding: 0; }
  html, body {
    width: 1200px; height: 800px; overflow: hidden;
    background: var(--stage);
    font-family: "Open Sans", Arial, sans-serif;
  }
  .canvas { position: relative; width: 1200px; height: 800px; }
  .hanger {
    position: absolute; top: 120px; width: 200px; height: 560px;
    border-radius: 9px; overflow: hidden;
    box-shadow: 0 6px 18px rgba(0,0,0,.25);
  }
  .hanger--front { left: 385px; background: var(--grass); }
  .hanger--back { left: 615px; background: var(--sky); color: #fff; }
  .hanger__base { position: absolute; inset: 0; }
  .sky-scene {
    position: absolute; left: 0; width: 200px; background: var(--sky);
  }
  .hanger--front .sky-scene { top: 0; height: 150px; }
  .hanger--back .sky-scene { top: 30px; height: 120px; }
  .brand {
    position: absolute; left: 0; right: 0; text-align: center;
    display: flex; justify-content: center; align-items: center; gap: 6px;
    font-weight: 700; font-size: 15px; color: var(--brand-red);
    letter-spacing: .2px;
  }
  .brand__dot {
    width: 10px; height: 10px; border-radius: 50%; background: var(--brand-red);
  }
  .hanger--front .brand { top: 205px; }
  .hanger--back .brand { top: 165px; }
  .contact-name {
    position: absolute; top: 335px; left: 0; right: 0; text-align: center;
    color: var(--ink); font-size: 16px; font-weight: 700;
  }
  .contact-name__role { font-weight: 400; font-size: 12px; }
  .contact-name__bar { font-weight: 400; margin: 0 3px; }
  .phone {
    position: absolute; left: 0; right: 0; text-align: center;
    font-size: 20px; font-weight: 700;
  }
  .hanger--front .phone { top: 428px; color: var(--ink); }
  .hanger--back .phone { top: 430px; color: #fff; }
  .address {
    position: absolute; left: 0; right: 0; text-align: center;
    font-size: 9px; line-height: 1.45;
  }
  .hanger--front .address { top: 495px; color: var(--ink); }
  .hanger--back .address { top: 478px; color: #fff; }
  .address__company { font-weight: 700; }
  .licenses {
    position: absolute; top: 12px; left: 12px;
    font-size: 7.5px; color: #fff;
  }
  .about {
    position: absolute; top: 202px; left: 14px; right: 14px;
    font-size: 10px; line-height: 1.6; text-align: justify; hyphens: auto;
  }
  .bottom-wave { position: absolute; left: 0; bottom: 0; }
</style>
</head>
<body>
<main class="canvas">

  <article class="hanger hanger--front">
    <svg class="hanger__base" width="200" height="560" viewBox="0 0 200 560" aria-hidden="true">
      <rect x="0" y="140" width="200" height="150" fill="#ffffff"/>
      <path d="M0 268 Q100 300 200 278" fill="none" stroke="#a7a9ac" stroke-width="5"/>
      <path d="M0 274 Q100 306 200 284 L200 560 L0 560 Z" fill="#8cc63f"/>
    </svg>
    <div class="sky-scene" role="img" aria-label="Sunny blue sky with a yellow sun and white clouds"></div>
    <div class="brand"><span class="brand__dot"></span>PINE LEDGER LLC</div>
    <p class="contact-name">Dale Corwin<span class="contact-name__bar">|</span><span class="contact-name__role">Director</span></p>
    <p class="phone">(888) 555-0142</p>
    <p class="address">
      <span class="address__company">PINE LEDGER LLC</span><br>
      240 W Orchard Ave Suite 118<br>
      Cedar Hollow, TX 75990
    </p>
  </article>

  <article class="hanger hanger--back">
    <p class="licenses">qbx5074316 &amp; qbz6081453</p>
    <div class="sky-scene" role="img" aria-label="Sunny blue sky with a yellow sun and white clouds"></div>
    <div class="brand"><span class="brand__dot"></span>PINE LEDGER LLC</div>
    <p class="about">We are dedicated to our customer and making sure that they get the best roof or general contracting experience possible. We believe in doing things the right way we are not about taking short cuts. In roofing this is absolutely necessary because most people know next to nothing about a roof. On wind and hail insurance claims give all of customer a 2 free upgrades we only use architectural shingles and a synthetic underlamenate. We use only Varnholt Ridgeline shingles</p>
    <p class="phone">(888) 555-0142</p>
    <p class="address">
      <span class="address__company">PINE LEDGER LLC</span><br>
      240 W Orchard Ave Suite 118<br>
      Cedar Hollow, TX 75990
    </p>
    <svg class="bottom-wave" width="200" height="40" viewBox="0 0 200 40" aria-hidden="true">
      <path d="M0 26 Q110 34 200 6" fill="none" stroke="#ffffff" stroke-width="2"/>
      <path d="M0 31 Q110 38 200 12 L200 40 L0 40 Z" fill="#ffffff"/>
    </svg>
  </article>

</main>
</body>
</html>
```